KORVEL Consulting Trucking Business Card

Our company name is KORVEL Consulting.

We need a business card design for our trucking company. The design should communicate reliability, stability and resourcefulness. The design should be clean, modern and industrial.

Audience will be US clients/prospects that require trucking to ship their products.

Target Market(s)

US businesses that needs trucks to ship products

Industry/Entity Type

Business

Font styles to use
Sans Serif

Colors
85cae6
3176b5
b7a5cd
85acd3
33a6d7

```html
<!DOCTYPE html>
<html lang="en">
<head>
<meta charset="utf-8">
<title>KORVEL Consulting – Business Card</title>
<link rel="stylesheet" href="https://fonts.googleapis.com/css2?family=Lato:wght@300;400;700&display=swap">
<style>
  :root {
    --card-blue: #3176b5;
    --panel-white: #ffffff;
    --brand-lavender: #8e66bb;
    --ink-dark: #2b2b2b;
    --rule-light: #c9d9ea;
    --text-light: #ffffff;
  }
  html, body {
    margin: 0;
    padding: 0;
    width: 679px;
    height: 1200px;
    overflow: hidden;
    background: var(--card-blue);
  }
  .card {
    position: relative;
    width: 679px;
    height: 1200px;
    background: var(--card-blue);
    font-family: "Lato", "Helvetica Neue", Arial, sans-serif;
    overflow: hidden;
  }
  .truck-illustration {
    position: absolute;
    left: 0;
    top: 131px;
    width: 590px;
    height: 439px;
    background: var(--panel-white);
  }
  .brand {
    position: absolute;
    left: 36px;
    top: 252px;
    margin: 0;
    line-height: 1;
  }
  .brand-name {
    display: block;
    font-weight: 700;
    font-size: 64px;
    letter-spacing: 1px;
    color: var(--brand-lavender);
  }
  .brand-tagline {
    display: block;
    margin-top: 12px;
    font-weight: 300;
    font-size: 70px;
    letter-spacing: 3px;
    color: var(--ink-dark);
  }
  .divider {
    position: absolute;
    left: 0;
    top: 572px;
    width: 679px;
    height: 2px;
    background: var(--rule-light);
  }
  .contact {
    position: absolute;
    left: 36px;
    top: 598px;
    margin: 0;
    padding: 0;
    list-style: none;
    font-weight: 300;
    font-size: 35px;
    line-height: 47px;
    color: var(--text-light);
  }
</style>
</head>
<body>
  <main class="card">
    <div class="truck-illustration" role="img" aria-label="White delivery truck illustration"></div>

    <h1 class="brand">
      <span class="brand-name">KORVEL</span>
      <span class="brand-tagline">CONSULTING</span>
    </h1>

    <div class="divider"></div>

    <ul class="contact">
      <li>Adress 1</li>
      <li>Phone Number</li>
      <li>website, etc</li>
      <li>Anything else you might</li>
      <li>want to add</li>
    </ul>
  </main>
</body>
</html>
```